Dubai Family protection infographic

We need to produce a way of attracting people to a life insurance and critical illness cover seminar. As this is a pretty dull subject for most people, so we need a cool way of getting people to read the invite/marketing collateral.

We're thinking some kind of colourful and attractive infographic that we can use on flyers and posters as well as online and as an emailer.

Content for the graphic is as bellow:

How much does it cost to replace Mum & Dad?

Mum = Chauffer, Cook, Laundry Service, Household Cleaner, Psychologist, Money Manager

Mums typically work a 94-hour week. At a rather paltry $12 per hour, that’s $4,888 per month – or $58,656 each year. (Source: wagelore.net)

Dad : The average Western Expat’s salary in the Gulf is $12,215 per month. That’s $146,580 each year. (Source: Palmcrest Ledger).

Did you know that the average age of critical illness claimants in the Middle East last year was just 48. Of these, 44% were for cancer while 41% were heart related.

The average age of a death claimant was just 50 years old.
(Source: Verenholt Assurance Group)

1 in 3 people will develop some form of cancer during their lifetime.

That’s 2.36 billion people globally.

And that’s equivalent to the population of China, USA, Brazil, Russia, Philippines, France, UK, South Africa and Italy combined.

Does your family have the resources to hand to cope if a tragedy happens to you?

What can you do to protect them and yourself?

Come to the UAE’s first national protection seminar to find out. Join us at Harbourline Riverside Sports Arena on June 19th at 19:00.

To pre-register, visit www.tovanmere.net/events or alternatively register on the door.

```html
<!DOCTYPE html>
<html lang="en">
<head>
<meta charset="utf-8">
<title>How much does it cost to replace Mum and Dad?</title>
<link rel="stylesheet" href="https://fonts.googleapis.com/css2?family=Oswald:wght@400;500;700&family=Open+Sans:wght@400;600;700&display=swap">
<style>
  :root {
    --cream: #f7efe0;
    --maroon: #8c2b1f;
    --orange: #e8892b;
    --orange-deep: #d9691f;
    --teal: #3bb0b7;
    --ink: #6b5a4a;
    --rule: #e7b98a;
  }
  * { margin: 0; padding: 0; box-sizing: border-box; }
  html, body { width: 1200px; height: 2400px; overflow: hidden; }
  body {
    background: var(--cream);
    font-family: "Open Sans", Arial, sans-serif;
    color: var(--ink);
    position: relative;
  }
  .abs { position: absolute; }
  .headline {
    left: 0; top: 50px; width: 1200px; text-align: center;
    font-family: "Oswald", "Arial Narrow", sans-serif; font-weight: 700;
    color: var(--maroon); font-size: 76px; line-height: 92px; letter-spacing: 1px;
  }
  .rule { background: var(--rule); height: 3px; }
  .section-label {
    font-family: "Oswald", sans-serif; font-weight: 500; font-size: 22px;
    color: var(--orange); letter-spacing: 1px;
  }
  .col-divider { left: 592px; top: 250px; width: 3px; height: 1530px; background: var(--rule); }
  .figure-fill { border-radius: 12px; }
  .mum-figure { left: 40px; top: 320px; width: 150px; height: 340px; background: linear-gradient(180deg, #ec9a45, var(--orange-deep)); }
  .dad-figure { left: 40px; top: 1320px; width: 150px; height: 360px; background: linear-gradient(180deg, #ec9a45, var(--orange-deep)); }
  .roles-title {
    left: 220px; top: 330px; font-family: "Oswald", sans-serif; font-weight: 700;
    font-size: 64px; line-height: 70px; color: var(--orange);
  }
  .roles-list {
    left: 220px; top: 410px; list-style: none;
    font-family: "Oswald", sans-serif; font-weight: 500; font-size: 40px; line-height: 44px; color: var(--teal);
  }
  .small { font-size: 22px; line-height: 28px; color: var(--ink); }
  .big-num { font-family: "Oswald", sans-serif; font-weight: 700; color: var(--orange); }
  .hours-note { left: 40px; top: 700px; width: 150px; text-align: right; }
  .hours-num { left: 200px; top: 690px; font-size: 190px; line-height: 200px; }
  .clock { left: 420px; top: 730px; }
  .hours-label { left: 200px; top: 880px; font-family: "Oswald", sans-serif; font-weight: 700; font-size: 44px; color: var(--teal); letter-spacing: 2px; }
  .at-note { left: 300px; top: 945px; }
  .rate-num { left: 150px; top: 960px; font-size: 120px; line-height: 130px; }
  .rate-label { left: 330px; top: 985px; font-family: "Oswald", sans-serif; font-weight: 700; font-size: 44px; line-height: 48px; color: var(--orange); }
  .dollar-rows { left: 40px; top: 1095px; font-family: "Oswald", sans-serif; font-weight: 700; font-size: 46px; line-height: 52px; color: var(--teal); letter-spacing: 6px; }
  .rate-totals { left: 300px; top: 1100px; font-size: 26px; line-height: 34px; color: var(--orange); }
  .rate-totals b { font-weight: 700; font-size: 30px; }
  .salary-intro { left: 220px; top: 1340px; width: 340px; text-align: center; font-size: 24px; line-height: 32px; }
  .salary-intro strong { color: var(--orange); font-size: 34px; line-height: 44px; font-family: "Oswald", sans-serif; }
  .salary-box { left: 220px; top: 1475px; width: 340px; height: 110px; background: var(--orange); color: #fff; display: flex; align-items: center; justify-content: center; gap: 14px; }
  .salary-box .amount { font-family: "Oswald", sans-serif; font-weight: 700; font-size: 64px; }
  .salary-box .unit { font-family: "Oswald", sans-serif; font-weight: 700; font-size: 28px; line-height: 30px; }
  .salary-year { left: 220px; top: 1595px; width: 340px; text-align: center; font-size: 22px; color: var(--orange); }
  .claim-intro { left: 640px; top: 320px; width: 360px; font-size: 24px; line-height: 32px; }
  .claim-intro b { color: var(--orange); }
  .claim-age { left: 1010px; top: 300px; font-size: 130px; line-height: 140px; }
  .of-these { left: 990px; top: 440px; }
  .funnel { left: 640px; top: 470px; }
  .funnel-label { font-family: "Oswald", sans-serif; font-weight: 700; font-size: 38px; line-height: 42px; }
  .cancer-label { left: 960px; top: 500px; color: var(--teal); }
  .cancer-label span, .heart-label span { display: block; font-family: "Open Sans", sans-serif; font-size: 22px; font-weight: 400; color: var(--ink); }
  .heart-label { left: 960px; top: 640px; color: var(--orange); }
  .death-intro { left: 640px; top: 810px; width: 240px; }
  .death-age { left: 900px; top: 790px; font-size: 140px; line-height: 150px; }
  .death-unit { left: 1040px; top: 815px; font-family: "Oswald", sans-serif; font-weight: 700; font-size: 44px; line-height: 50px; color: var(--orange); }
  .odds-box { left: 640px; top: 965px; width: 220px; height: 90px; background: var(--orange); color: #fff; font-family: "Oswald", sans-serif; font-weight: 700; font-size: 60px; display: flex; align-items: center; justify-content: center; }
  .odds-people { left: 890px; top: 940px; width: 270px; height: 150px; border-radius: 10px; background: linear-gradient(90deg, var(--teal) 0%, var(--teal) 66%, var(--orange) 66%); }
  .odds-note { left: 640px; top: 1070px; width: 330px; }
  .global-prefix { left: 640px; top: 1150px; }
  .global-num { left: 640px; top: 1170px; font-family: "Oswald", sans-serif; font-weight: 700; font-size: 96px; line-height: 104px; color: var(--teal); }
  .global-note { left: 640px; top: 1275px; }
  .world-map { left: 640px; top: 1320px; width: 520px; height: 310px; border-radius: 12px; background: linear-gradient(135deg, #f0a558, var(--orange-deep)); }
  .map-note { left: 640px; top: 1650px; width: 520px; }
  .invite-rule { left: 40px; top: 1830px; width: 1120px; }
  .invite { left: 40px; top: 1880px; width: 1120px; font-size: 30px; line-height: 44px; color: var(--orange); }
  .invite p { margin-bottom: 28px; }
  .invite strong { font-weight: 700; }
</style>
</head>
<body>
  <h1 class="abs headline">HOW MUCH DOES IT COST TO<br>REPLACE MUM AND DAD?</h1>
  <div class="abs rule" style="left:40px;top:240px;width:1120px;"></div>
  <div class="abs col-divider"></div>

  <!-- Mums -->
  <div class="abs section-label" style="left:40px;top:258px;">MUMS</div>
  <div class="abs figure-fill mum-figure" role="img" aria-label="Figure of a mother"></div>
  <div class="abs roles-title">MUM'S ARE:</div>
  <ul class="abs roles-list">
    <li>Cooks</li><li>Chauffers</li><li>Psychologists</li><li>Laundry Services</li><li>Money Managers</li><li>Household Cleaners</li>
  </ul>
  <div class="abs small hours-note">Mum's typically work</div>
  <div class="abs big-num hours-num">94</div>
  <svg class="abs clock" width="140" height="140" viewBox="0 0 140 140" aria-hidden="true">
    <circle cx="70" cy="70" r="60" fill="none" stroke="var(--teal)" stroke-width="12"/>
    <path d="M70 32 V72 H100" fill="none" stroke="var(--teal)" stroke-width="12" stroke-linecap="round"/>
  </svg>
  <div class="abs hours-label">HOURS PER WEEK</div>
  <div class="abs small at-note">At</div>
  <div class="abs big-num rate-num">$12</div>
  <div class="abs rate-label">PER<br>HOUR</div>
  <div class="abs dollar-rows">$$$$$$<br>$$$$$$</div>
  <div class="abs rate-totals">that's <b>$4,888</b><br>per month<br>or <b>$58,656</b><br>each year.</div>

  <!-- Dads -->
  <div class="abs rule" style="left:40px;top:1240px;width:530px;"></div>
  <div class="abs section-label" style="left:40px;top:1260px;">DADS</div>
  <div class="abs figure-fill dad-figure" role="img" aria-label="Figure of a father"></div>
  <div class="abs small salary-intro">The average<br><strong>Western Expat's</strong><br>salary in the Gulf is</div>
  <div class="abs salary-box"><span class="amount">$12,215</span><span class="unit">PER<br>MONTH</span></div>
  <div class="abs salary-year">That's $146,580 each year.</div>

  <!-- Deaths -->
  <div class="abs section-label" style="left:640px;top:258px;">DEATHS</div>
  <div class="abs small claim-intro">Did you know that the average age of <b>critical illness claimants</b> in the Middle East last year was just</div>
  <div class="abs big-num claim-age">48</div>
  <div class="abs small of-these">Of these,</div>
  <svg class="abs funnel" width="300" height="300" viewBox="0 0 300 300" aria-label="Share of critical illness claims">
    <polygon points="40,0 260,0 300,40 250,140 50,140 0,40" fill="var(--teal)"/>
    <polygon points="50,150 250,150 200,300 100,300" fill="var(--orange)"/>
    <text x="150" y="92" text-anchor="middle" font-family="Oswald, sans-serif" font-weight="700" font-size="62" fill="#fff">44%</text>
    <text x="150" y="240" text-anchor="middle" font-family="Oswald, sans-serif" font-weight="700" font-size="62" fill="#fff">41%</text>
  </svg>
  <div class="abs funnel-label cancer-label"><span>were for</span>cancer</div>
  <div class="abs funnel-label heart-label"><span>were</span>heart<br>related.</div>

  <div class="abs small death-intro">The average age of a death claimant was just</div>
  <div class="abs big-num death-age">50</div>
  <div class="abs death-unit">YEARS<br>OLD</div>

  <div class="abs odds-box">1 in 3</div>
  <div class="abs odds-people" role="img" aria-label="Three people, one of them highlighted"></div>
  <div class="abs small odds-note">people will develop some form of cancer during their lifetime.</div>
  <div class="abs small global-prefix">That's</div>
  <div class="abs global-num">2.36 Billion</div>
  <div class="abs small global-note">people globally.</div>
  <div class="abs world-map" role="img" aria-label="World map highlighting the named countries"></div>
  <div class="abs small map-note">And that's equivalent to the population of China, USA, Brazil, Russia, Philippines, France, UK, South Africa and Italy combined.</div>

  <!-- Invitation -->
  <div class="abs rule invite-rule"></div>
  <div class="abs invite">
    <p>Does your family have the resources to hand to cope if a tragedy happens to <strong>you</strong>? What can you do to protect them and yourself? Come to the UAE's first national protection seminar to find out.</p>
    <p><strong>Join us at Harbourline Riverside Sports Arena on June 19th at 19:00.</strong></p>
    <p>To pre-register, visit <strong>www.tovanmere.net/events</strong> or alternatively register at the door.</p>
  </div>
</body>
</html>
```